Flyer design

We need a new flyer designed. We are not happy with our current design. We want to keep the pictures and basic info, just new design.

Target Market(s)

primarily multi family and HOA,s

Industry/Entity Type

Construction Company

Requirements
Must have
• Must have photos uploaded and use the text on the previous flyer. (also uploaded)

```html
<!DOCTYPE html>
<html lang="en">
<head>
<meta charset="utf-8">
<title>Corvane Construction Flyer</title>
<link rel="stylesheet" href="https://fonts.googleapis.com/css2?family=Roboto+Condensed:wght@700&family=Lato:wght@300;400;700&display=swap">
<style>
  :root {
    --brand-blue: #1672e6;
    --deep-blue: #0d3d8c;
    --ink: #2a2a2a;
    --band-dark: #5c5c5c;
    --band-light: #a9a9a9;
    --sky: #4f8ee6;
    --roof: #3a3a3c;
    --vest: #b9e02a;
  }
  * { margin: 0; padding: 0; box-sizing: border-box; }
  html, body { width: 896px; height: 1200px; overflow: hidden; background: #ffffff; }
  .flyer {
    position: relative;
    width: 896px;
    height: 1200px;
    overflow: hidden;
    font-family: "Lato", sans-serif;
    color: var(--ink);
    background: linear-gradient(135deg, #f4f4f4 0%, #dcdcdc 45%, #efefef 70%, #d4d4d4 100%);
  }
  .header {
    position: absolute; left: 0; top: 0; width: 896px; height: 140px; background: #fff;
  }
  .brand { position: absolute; left: 32px; top: 36px; display: flex; align-items: center; gap: 14px; }
  .brand-square { width: 52px; height: 52px; background: var(--brand-blue); }
  .brand-name { font-family: "Lato", sans-serif; font-weight: 700; font-size: 46px; line-height: 1; color: var(--brand-blue); }
  .brand-sub { font-family: "Lato", sans-serif; font-weight: 300; font-size: 16px; color: #555; margin-top: 2px; }
  .photos { position: absolute; left: 0; top: 0; }
  .section-title {
    position: absolute; left: 37px;
    font-family: "Roboto Condensed", sans-serif; font-weight: 700;
    font-size: 32px; color: var(--brand-blue); letter-spacing: 0.3px;
  }
  .list-item {
    position: absolute; font-size: 13px; color: #333; padding-left: 24px; line-height: 1.2;
  }
  .list-item::before {
    content: ""; position: absolute; left: 2px; top: -4px; width: 1px; height: 22px; background: var(--deep-blue);
  }
  .list-item::after {
    content: ""; position: absolute; left: -1px; top: 4px; width: 7px; height: 7px;
    background: var(--brand-blue); transform: rotate(45deg);
  }
  .info-band {
    position: absolute; left: 0; top: 918px; width: 896px; height: 184px;
    background: linear-gradient(180deg, var(--band-dark) 0%, var(--band-light) 55%, var(--band-dark) 100%);
  }
  .info-col { position: absolute; top: 32px; color: #fff; }
  .info-title { font-family: "Roboto Condensed", sans-serif; font-weight: 700; font-size: 30px; margin-bottom: 10px; }
  .info-line { font-weight: 300; font-size: 19px; line-height: 24px; }
  .contact-line { font-weight: 700; font-size: 19px; line-height: 26px; display: flex; align-items: center; gap: 6px; }
  .contact-line.small { font-size: 16px; }
  .tagline-band {
    position: absolute; left: 0; top: 1102px; width: 896px; height: 98px;
    background: linear-gradient(135deg, #ffffff, #e6e6e6);
    display: flex; align-items: center; justify-content: center;
    font-family: "Roboto Condensed", sans-serif; font-weight: 700; font-size: 27px;
  }
  .tagline-band .blue { color: var(--brand-blue); }
  .tagline-band .dark { color: #222; }
</style>
</head>
<body>
<main class="flyer">
  <div class="header">
    <div class="brand">
      <span class="brand-square"></span>
      <div>
        <div class="brand-name">Corvane</div>
        <div class="brand-sub">Construction Services Inc.</div>
      </div>
    </div>
  </div>

  <svg class="photos" width="896" height="580" viewBox="0 0 896 580">
    <defs>
      <linearGradient id="roofPhoto" x1="0" y1="0" x2="0" y2="1">
        <stop offset="0" stop-color="#3f86e8"/>
        <stop offset="0.4" stop-color="#6ea2e6"/>
        <stop offset="0.6" stop-color="#4a4a4e"/>
        <stop offset="1" stop-color="#2e2e30"/>
      </linearGradient>
      <linearGradient id="crewPhoto" x1="0" y1="0" x2="1" y2="1">
        <stop offset="0" stop-color="#2a63d6"/>
        <stop offset="0.5" stop-color="#6c93d9"/>
        <stop offset="0.75" stop-color="#9cc22e"/>
        <stop offset="1" stop-color="#1f2f55"/>
      </linearGradient>
    </defs>
    <polygon points="0,131 630,89 612,484 0,542" fill="url(#roofPhoto)" role="img" aria-label="Photo of roofers replacing shingles on a house roof under a blue sky"/>
    <polygon points="660,0 896,0 896,565 620,565 645,484 545,490" fill="url(#crewPhoto)" stroke="var(--brand-blue)" stroke-width="3" role="img" aria-label="Photo of two construction workers in hard hats and safety vests pointing at a site"/>
    <line x1="660" y1="0" x2="545" y2="490" stroke="var(--brand-blue)" stroke-width="4"/>
  </svg>

  <h2 class="section-title" style="top:560px;">THE BUILDING ADVANTAGE:</h2>
  <div class="list-item" style="left:43px; top:620px;">Hands on approach</div>
  <div class="list-item" style="left:43px; top:650px;">High Level of communication with client</div>
  <div class="list-item" style="left:361px; top:620px;">Daily or weekly updates on every project</div>
  <div class="list-item" style="left:361px; top:650px;">Competitive pricing</div>
  <div class="list-item" style="left:694px; top:620px;">Due diligence</div>
  <div class="list-item" style="left:694px; top:650px;">Single source for all needs</div>

  <h2 class="section-title" style="top:714px;">SERVICES WE PROVIDE:</h2>
  <div class="list-item" style="left:43px; top:770px;">Roof replacements</div>
  <div class="list-item" style="left:43px; top:800px;">Concrete repairs</div>
  <div class="list-item" style="left:43px; top:832px;">Office and clubhouse remodeling</div>
  <div class="list-item" style="left:43px; top:861px;">Fire and flood damage build back</div>
  <div class="list-item" style="left:361px; top:770px;">Consulting services</div>
  <div class="list-item" style="left:361px; top:800px;">Budget proposals</div>
  <div class="list-item" style="left:361px; top:832px;">Asphalt paving</div>
  <div class="list-item" style="left:361px; top:861px;">Dog parks</div>
  <div class="list-item" style="left:669px; top:770px;">Exterior siding and carpentry</div>
  <div class="list-item" style="left:669px; top:800px;">Exterior/interior paint</div>
  <div class="list-item" style="left:669px; top:832px;">Large scale interior<br>renovations</div>

  <section class="info-band">
    <div class="info-col" style="left:37px;">
      <div class="info-title">California Address</div>
      <div class="info-line">480 Harbor Ridge Blvd.</div>
      <div class="info-line">Suite 210</div>
      <div class="info-line">Costa Mesa, CA. 92626</div>
    </div>
    <div class="info-col" style="left:335px;">
      <div class="info-title">Texas Address</div>
      <div class="info-line">1870 Cedar Bend Rd.</div>
      <div class="info-line">Suite 105-220</div>
      <div class="info-line">Spring TX. 77380</div>
    </div>
    <div class="info-col" style="left:591px;">
      <div class="info-title">Contact</div>
      <div class="contact-line">
        <svg width="12" height="12" viewBox="0 0 12 12" aria-hidden="true"><circle cx="6" cy="6" r="5.2" fill="none" stroke="#fff" stroke-width="1"/><path d="M4 3.2 L5 3 L5.6 4.6 L5 5.1 Q5.6 6.4 6.9 7 L7.4 6.4 L9 7 L8.8 8 Q6 8.4 3.9 5.9 Q3.4 4.5 4 3.2Z" fill="#fff"/></svg>
        (714) 555-0142
      </div>
      <div class="contact-line small">
        <svg width="12" height="12" viewBox="0 0 12 12" aria-hidden="true"><circle cx="6" cy="6" r="5" fill="none" stroke="#fff" stroke-width="1.2"/><ellipse cx="6" cy="6" rx="2" ry="5" fill="none" stroke="#fff" stroke-width="1"/><line x1="1" y1="6" x2="11" y2="6" stroke="#fff" stroke-width="1"/></svg>
        www.corvaneconstruction.com
      </div>
    </div>
  </section>

  <footer class="tagline-band">
    <span class="blue">General Contractor.</span>&nbsp;<span class="dark">Multifamily.</span>&nbsp;<span class="blue">Commercial.</span>&nbsp;<span class="dark">Residential.</span>&nbsp;<span class="blue">Due Diligence.</span>
  </footer>
</main>
</body>
</html>
```